Brackenmoor.com.au - Quorvel Australia - Uncoded PSD only

We need a web design for a virtual assistant company based in Sydney Australia called "Brackenmoor". We provide virtual assistance and unlimited admin tasks to small business owners for a monthly fee. We would like to see designs that are not too different to www.quorvel.com. Words to describe the design and feel of this website are sleek and professional. We want to use bright inviting colours for the call to action buttons and a professional business focused background.

Target Market(s)

business executives, business owners, small business owners, those professionals who lack time.

Industry/Entity Type

Business Consultant

Number of Pages Required

3 page

Font styles to use
Sans Serif

Colors
5e5e5e
1b1b1b
3176b5
33b8a4

Requirements
Must have
• Call to action buttons, sleek business feel think plovix.io and quorvel.com
Nice to have
• Bold back ground colours, bright call to action buttons
Should not have
• too much white

```html
<!DOCTYPE html>
<html lang="en">
<head>
<meta charset="utf-8">
<title>Brackenmoor – Virtual Assistance</title>
<link href="https://fonts.googleapis.com/css2?family=Roboto:wght@300;400;500;700&display=swap" rel="stylesheet">
<style>
:root{
  --blue:#3176b5;
  --teal:#33b8a4;
  --green:#2ecc71;
  --ink:#1b1b1b;
  --grey:#5e5e5e;
  --light:#f4f6f8;
  --line:#d9dde1;
  --white:#ffffff;
}
*{box-sizing:border-box;margin:0;padding:0}
html,body{width:1200px;height:3260px;overflow:hidden}
body{font-family:"Roboto",Arial,sans-serif;color:var(--grey);background:var(--white)}
.section{position:relative;width:1200px;overflow:hidden}
.photo{position:absolute}

/* header + hero */
.hero{height:580px}
.hero .photo{inset:0;background:linear-gradient(120deg,#c9ced3 0%,#8d969e 45%,#4d5560 100%)}
.hero-shade{position:absolute;inset:0;background:rgba(20,30,40,.35)}
.site-nav{position:absolute;top:0;left:0;right:0;height:80px;background:rgba(20,24,28,.55);display:flex;align-items:center;padding:0 40px;color:var(--white)}
.brand{font-size:26px;font-weight:400;color:var(--teal);margin-right:auto}
.nav-links{display:flex;gap:34px;font-size:13px;font-weight:500;letter-spacing:.5px;margin-right:26px}
.btn-plans{background:var(--green);color:var(--white);font-size:13px;font-weight:500;padding:11px 18px;border-radius:2px;margin-right:28px}
.nav-phone{font-size:18px;font-weight:500}
.hero-copy{position:absolute;top:205px;left:0;right:0;text-align:center;color:var(--white)}
.hero-copy h1{font-size:48px;font-weight:500;margin-bottom:14px}
.hero-copy p{font-size:27px;font-weight:300;line-height:1.3;width:760px;margin:0 auto 34px}
.btn-solid{display:inline-block;background:var(--teal);color:var(--white);font-size:17px;font-weight:400;padding:16px 34px;border-radius:2px}
.dots{position:absolute;bottom:56px;left:0;right:0;display:flex;justify-content:center;gap:10px}
.dots span{width:11px;height:11px;border-radius:50%;background:rgba(255,255,255,.5)}
.dots span:first-child{background:var(--white)}

/* feature bands */
.feature{height:420px;color:var(--white)}
.feature h2{font-size:31px;font-weight:700;line-height:1.2;margin-bottom:20px;color:var(--white)}
.feature p{font-size:14px;line-height:1.7;color:var(--white)}
.feature .copy{position:absolute;top:62px;width:590px}
.btn-outline{display:inline-block;margin-top:28px;border:2px solid var(--white);color:var(--white);font-size:15px;padding:12px 24px;border-radius:2px}
.feature-blue{background:var(--blue)}
.feature-blue .copy{left:72px}
.feature-blue .photo{right:0;top:0;width:520px;height:420px;background:linear-gradient(90deg,var(--blue) 0%,#dfe7ee 40%,#f4f4f4 100%)}
.feature-teal{height:440px;background:var(--teal)}
.feature-teal .copy{left:540px;top:70px}
.feature-teal .photo{left:0;top:0;width:520px;height:440px;background:linear-gradient(90deg,#eef1f3 0%,#cfd8dc 60%,var(--teal) 100%)}
.feature-dark{height:420px;background:#2a2d30}
.feature-dark .copy{left:72px}
.feature-dark .photo{right:0;top:0;width:520px;height:420px;background:linear-gradient(90deg,#2a2d30 0%,#bfc4c8 45%,#e9ecee 100%)}

/* price band */
.price{height:272px}
.price .photo{inset:0;background:linear-gradient(90deg,#3b3a3c,#6a6668 50%,#3b3a3c)}
.price-box{position:absolute;left:252px;top:78px;width:696px;height:116px;border:3px solid rgba(255,255,255,.8);display:flex;align-items:center;justify-content:center;font-size:66px;font-weight:300;color:var(--teal);background:rgba(0,0,0,.2)}

/* clients */
.clients{height:228px;padding-top:40px;text-align:center}
.clients h3{font-size:22px;font-weight:500;color:var(--blue);margin-bottom:48px}
.client-row{display:flex;justify-content:center;align-items:center;gap:54px;color:#9a9ea2;font-size:26px;font-weight:500}
.client-row span{display:flex;align-items:center;gap:10px}
.client-row i{display:inline-block;width:24px;height:24px;background:#b2b6ba}

/* testimonials */
.testimonials{height:380px;background:var(--white);display:flex;justify-content:center;gap:30px;padding-top:40px}
.quote{width:330px;text-align:center}
.avatar{width:96px;height:96px;border-radius:50%;margin:0 auto -40px;position:relative;z-index:1;border:4px solid var(--white);background:linear-gradient(160deg,#d7dde2,#9aa4ad)}
.quote-card{border:1px solid var(--line);padding:56px 26px 26px;font-size:13px;line-height:1.6;color:var(--grey);height:166px}
.quote-name{margin-top:28px;color:var(--blue);font-size:18px;font-weight:500}
.quote-role{font-size:12px;color:#8a8e92;margin-top:4px}

/* call to action */
.cta{height:220px;text-align:center;padding-top:44px}
.cta h2{font-size:38px;font-weight:500;color:var(--blue)}
.cta p{font-size:16px;color:var(--grey);margin:10px 0 24px}

/* footer */
.site-footer{height:300px;background:var(--ink);color:#a7aaad;padding:44px 72px 0}
.footer-cols{display:flex;gap:0}
.footer-col{width:264px;font-size:12px;line-height:2}
.footer-col h4{color:var(--white);font-size:17px;font-weight:500;margin-bottom:8px}
.footer-col strong{color:var(--white);font-weight:500}
.footer-bottom{position:absolute;left:72px;right:72px;bottom:28px;display:flex;justify-content:space-between;align-items:center;font-size:11px;border-top:1px solid #33363a;padding-top:18px}
.social{display:flex;gap:10px}
.social span{width:32px;height:32px;border-radius:50%;border:1px solid #6d7074}
</style>
</head>
<body>

<header class="section hero">
  <div class="photo" role="img" aria-label="Photo of a businessman in a suit working at a desk"></div>
  <div class="hero-shade"></div>
  <nav class="site-nav">
    <div class="brand">Brackenmoor</div>
    <div class="nav-links"><span>HOME</span><span>WHO WE ARE</span><span>WHAT WE DO</span><span>WHY BRACKENMOOR</span></div>
    <div class="btn-plans">PRICING &amp; PLANS</div>
    <div class="nav-phone">PH: 123-456-7890</div>
  </nav>
  <div class="hero-copy">
    <h1>Virtual Assistance &amp; Unlimited Admin Tasks</h1>
    <p>We are a virtual assistant company based in Sydney Australia to small business owners for a monthly fee</p>
    <span class="btn-solid">Request a Consultation</span>
  </div>
  <div class="dots"><span></span><span></span><span></span></div>
</header>

<section class="section feature feature-blue">
  <div class="copy">
    <h2>Suspendisse lobortis turpis in odio<br>interdum lorem euismod</h2>
    <p>Aliquam molestie, mi et imperdiet euismod, dui purus auctor tellus, at interdum lorem ipsum dolor. Sed consectetur sollicitudin sapien, sit amet adipiscing nunc gravida ut. Integer aliquam ultricies magna, non facilisis leo rutrum in. Cras vitae lorem eget dui viverra dictum. Vivamus egestas turpis in magna varius commodo. Sed semper viverra egestas.</p>
    <span class="btn-outline">LEARN MORE</span>
  </div>
  <div class="photo" role="img" aria-label="Photo of a smiling businesswoman"></div>
</section>

<section class="section price">
  <div class="photo" role="img" aria-label="Dim photo of a team of office workers"></div>
  <div class="price-box">Starting at $749/mo.</div>
</section>

<section class="section clients">
  <h3>Assistants are used by busy people from amazing companies all over the world.</h3>
  <div class="client-row">
    <span>Brindle</span>
    <span>Vantor</span>
    <span><i></i>Ashcombe University</span>
    <span>Kestra</span>
    <span>Pelmar</span>
    <span>Covewell Investments</span>
  </div>
</section>

<section class="section feature feature-teal">
  <div class="photo" role="img" aria-label="Photo of a young man holding a tablet"></div>
  <div class="copy">
    <h2>Suspendisse lobortis turpis in odio<br>interdum lorem euismod</h2>
    <p>Aliquam molestie, mi et imperdiet euismod, dui purus auctor tellus, at interdum lorem ipsum dolor. Sed consectetur sollicitudin sapien, sit amet adipiscing nunc gravida ut. Integer aliquam ultricies magna, non facilisis leo rutrum in. Cras vitae lorem eget dui viverra dictum. Vivamus egestas turpis in magna varius commodo. Sed semper viverra egestas.</p>
    <span class="btn-outline">LEARN MORE</span>
  </div>
</section>

<section class="section testimonials">
  <article class="quote">
    <div class="avatar" role="img" aria-label="Portrait of a client"></div>
    <div class="quote-card">Aenean a vel eget cursus sem ultrices sed justo. Vestibulum porta nulla ultrices tincidunt sed laoreet vel dolor. Suspendisse lobortis turpis in odio.</div>
    <div class="quote-name">Evan Hollis</div>
    <div class="quote-role">Partner &amp; CEO</div>
  </article>
  <article class="quote">
    <div class="avatar" role="img" aria-label="Portrait of a client"></div>
    <div class="quote-card">Aenean a vel eget cursus sem ultrices sed justo. Vestibulum porta nulla ultrices tincidunt sed laoreet vel dolor. Suspendisse lobortis turpis in odio.</div>
    <div class="quote-name">Evan Hollis</div>
    <div class="quote-role">Partner &amp; CEO</div>
  </article>
  <article class="quote">
    <div class="avatar" role="img" aria-label="Portrait of a client"></div>
    <div class="quote-card">Aenean a vel eget cursus sem ultrices sed justo. Vestibulum porta nulla ultrices tincidunt sed laoreet vel dolor. Suspendisse lobortis turpis in odio.</div>
    <div class="quote-name">Evan Hollis</div>
    <div class="quote-role">Partner &amp; CEO</div>
  </article>
</section>

<section class="section feature feature-dark">
  <div class="copy">
    <h2>Suspendisse lobortis turpis in odio<br>interdum lorem euismod</h2>
    <p>Aliquam molestie, mi et imperdiet euismod, dui purus auctor tellus, at interdum lorem ipsum dolor. Sed consectetur sollicitudin sapien, sit amet adipiscing nunc gravida ut. Integer aliquam ultricies magna, non facilisis leo rutrum in. Cras vitae lorem eget dui viverra dictum. Vivamus egestas turpis in magna varius commodo. Sed semper viverra egestas.</p>
    <span class="btn-outline">LEARN MORE</span>
  </div>
  <div class="photo" role="img" aria-label="Photo of a hand using a tablet"></div>
</section>

<section class="section cta">
  <h2>Are you ready to supercharge your productivity?</h2>
  <p>Vivamus egestas risus in magna varius commodo. Sed semper viverra egestas.</p>
  <span class="btn-solid">Request a Consultation</span>
</section>

<footer class="section site-footer">
  <div class="footer-cols">
    <div class="footer-col">
      <h4>About Brackenmoor</h4>
      Our Story<br>Our Assistants<br>Our Happy Clients<br>Our Partner Network<br>Our Guarantee
    </div>
    <div class="footer-col">
      <h4>Company</h4>
      Press<br>Blog<br>Careers
    </div>
    <div class="footer-col">
      <h4>Policies</h4>
      Terms of Service<br>Privacy Policy<br>Security
    </div>
    <div class="footer-col">
      <h4>Contact Us</h4>
      <strong>Client Happiness Team</strong><br>hello@brackenmoor.com.au<br>
      <strong>Sales Team</strong><br>sales@brackenmoor.com.au<br>
      Ph: 123-456-7890
    </div>
  </div>
  <div class="footer-bottom">
    <span>Copyright © 2015 Brackenmoor. All Rights Reserved.</span>
    <div class="social"><span></span><span></span><span></span></div>
  </div>
</footer>

</body>
</html>
```